Kestrafab, NSW. Manufacturing/Construction industry. Require 4 page brochure/flyer

www.kestrafab.com.au - see website for branding/colours
Require a double sided A3 folded - so 4 x A4 page brochure on the company to provide to potential clients showcasing our capabilities.
I have an idea what I would like, but am not a graphic designer so struggle with making it look attractive.
Page 1: Photo of shed steelwork + logo, company name etc
Page 2: Who we are, where we are, capabilities and technological advantages
Page 3: What we do, what we will do for the new client
Page 4: Photo with contact details
I dont mind if the designer can create the basic design and can fill in the details later once the design is finalised.
Have uploaded some basic photos similar to what I could use, however they are low quality so would need higher resolution. Also uploaded a basic flyer we currently use to show previously completed projects just for information.

Target Market(s)

Developers

Industry/Entity Type

Manufacturing

Font styles to use
Other font styles liked:
• OpenSans

Colors
0355a3
3377b5
85acd3

Requirements
Must have
• 4 x A4 pages, pages 2 and 3 to be A3 size, so flow together.
Nice to have
• Have attached capability brochure that we currently use. The new one will need to be similar level of professionalism, however less words/details

```html
<!DOCTYPE html>
<html lang="en">
<head>
<meta charset="utf-8">
<title>Kestrafab Capability Brochure</title>
<link href="https://fonts.googleapis.com/css2?family=Oswald:wght@500;600&family=Open+Sans:ital,wght@0,400;0,600;0,700;1,400&display=swap" rel="stylesheet">
<style>
  :root{
    --canvas:#e4e5e6;
    --navy:#174b75;
    --navy-deep:#0f3b60;
    --navy-light:#23608f;
    --blue:#3377b5;
    --sky:#5fb4dc;
    --paper:#f2f3f5;
    --white:#ffffff;
    --ink:#4d5864;
    --muted:#8a95a1;
  }
  *{margin:0;padding:0;box-sizing:border-box}
  html,body{width:1200px;height:2536px;overflow:hidden}
  body{background:var(--canvas);position:relative;font-family:"Open Sans",Arial,sans-serif;color:var(--ink)}
  .page{position:absolute;overflow:hidden;box-shadow:0 6px 18px rgba(0,0,0,.18)}
  .page--single{width:500px;height:707px}
  .page--spread{width:1000px;height:707px}
  .half{position:absolute;top:0;width:500px;height:707px;overflow:hidden}
  .half--left{left:0}
  .half--right{left:500px}
  .shapes{position:absolute;inset:0;width:100%;height:100%}
  .heading{font-family:"Oswald",Arial,sans-serif;font-weight:600;text-transform:uppercase;letter-spacing:.3px}

  /* brand lockup */
  .brand{position:absolute;display:flex;align-items:center;gap:10px}
  .brand__mark{width:34px;height:34px;border-radius:50%;background:var(--white)}
  .brand__name{font-family:"Oswald",Arial,sans-serif;font-weight:600;font-size:19px;color:var(--white);letter-spacing:.5px;line-height:1}
  .brand__tag{font-size:6.5px;letter-spacing:1px;color:var(--white);opacity:.85;margin-top:3px}
  .brand--navy .brand__mark{background:var(--navy)}
  .brand--navy .brand__name,.brand--navy .brand__tag{color:var(--navy)}

  /* cover */
  .cover__claim{position:absolute;left:60px;top:560px;color:var(--white);font-size:16px;line-height:1.3}
  .cover__claim strong{display:block;font-size:15px}
  .cover__web{position:absolute;left:45px;top:640px;width:330px;height:32px;background:var(--white);display:flex;align-items:center;gap:10px;padding-left:16px;font-size:13px;letter-spacing:1px;color:var(--navy);font-weight:600}

  /* back cover */
  .expertise__label{position:absolute;left:30px;top:40px;font-size:8px;color:var(--muted);text-transform:uppercase;letter-spacing:1px}
  .expertise__list{position:absolute;left:30px;top:58px;list-style:none;font-size:9px;font-weight:700;color:var(--navy);line-height:15.5px}
  .expertise__list li{border-bottom:1px solid #c9d1d9;width:135px}
  .expertise__title{position:absolute;left:190px;top:42px;font-size:15px;color:var(--navy)}
  .expertise__body{position:absolute;left:190px;top:70px;width:285px;font-size:8px;line-height:12px;color:var(--ink)}
  .expertise__body p{margin-bottom:7px}
  .contact{position:absolute;right:40px;top:575px;text-align:right;color:var(--white)}
  .contact__title{font-size:19px;margin-bottom:8px}
  .contact__row{display:flex;justify-content:flex-end;align-items:center;gap:8px;font-size:11px;line-height:20px}
  .contact__icon{width:14px;height:14px;background:var(--white);border-radius:2px;display:inline-block}
  .contact__address{position:absolute;left:30px;bottom:28px;color:var(--white);font-size:11px}

  /* inside left */
  .about__title{position:absolute;left:40px;top:95px;font-size:24px;color:var(--navy)}
  .about__lead{position:absolute;left:40px;top:132px;width:420px;font-size:11px;color:var(--blue);font-style:italic}
  .about__body{position:absolute;left:40px;top:162px;width:420px;font-size:9px;line-height:14px}
  .about__band{position:absolute;left:40px;top:255px;color:var(--white);font-size:12px;font-family:"Oswald",Arial,sans-serif;font-weight:500;letter-spacing:.6px}
  .about__detail{position:absolute;left:40px;top:295px;width:420px;font-size:9px;line-height:14px}
  .values{position:absolute;left:30px;top:560px;width:440px;display:flex;justify-content:space-between;color:var(--white);text-align:center}
  .value{width:130px}
  .value svg{display:block;margin:0 auto 6px}
  .value__name{font-size:12px;margin-bottom:4px}
  .value__text{font-size:8px;line-height:11px;opacity:.9}

  /* inside right */
  .projects{position:absolute;left:45px;top:55px;width:420px;color:var(--white)}
  .projects__title{font-size:24px}
  .projects__steps{font-size:9px;letter-spacing:1.5px;color:var(--sky);font-weight:600;margin:2px 0 10px}
  .projects__lead{font-size:12px;font-weight:700;margin-bottom:14px}
  .ticks{list-style:none;font-size:9px;line-height:13px}
  .ticks li{display:flex;gap:8px;margin-bottom:10px}
  .tick{flex:none;width:11px;height:11px;border:1px solid var(--white);border-radius:50%;position:relative;margin-top:1px}
  .tick::after{content:"";position:absolute;left:3px;top:1px;width:3px;height:5px;border:solid var(--white);border-width:0 1.2px 1.2px 0;transform:rotate(45deg)}
  .inhouse{position:absolute;left:60px;top:610px;list-style:none;font-size:9px;line-height:17px;color:var(--ink)}
  .inhouse li{display:flex;gap:8px;align-items:center}
  .inhouse .tick{border-color:var(--navy)}
  .inhouse .tick::after{border-color:var(--navy)}
</style>
</head>
<body>

<!-- Front cover -->
<section class="page page--single" style="left:350px;top:70px">
  <svg class="shapes" viewBox="0 0 500 707" preserveAspectRatio="none">
    <defs>
      <linearGradient id="stairA" x1="0" y1="0" x2="1" y2="0.3">
        <stop offset="0" stop-color="#2a2c30"/><stop offset=".45" stop-color="#9ea3a8"/><stop offset=".75" stop-color="#e6e8ea"/><stop offset="1" stop-color="#f7f7f7"/>
      </linearGradient>
    </defs>
    <rect width="500" height="707" fill="var(--navy)"/>
    <polygon points="0,0 500,0 500,70 0,150" fill="var(--navy-light)"/>
    <polygon role="img" aria-label="Photo: spiral glass staircase in a bright modern interior" points="45,165 500,75 500,450 45,530" fill="url(#stairA)"/>
    <polygon points="320,482 500,448 500,560" fill="var(--sky)"/>
    <polygon points="0,707 0,640 500,575 500,707" fill="var(--navy-deep)"/>
  </svg>
  <div class="brand" style="left:270px;top:28px">
    <span class="brand__mark"></span>
    <div><div class="brand__name">KESTRAFAB GROUP</div><div class="brand__tag">INNOVATION | COMMITMENT | PRECISION</div></div>
  </div>
  <p class="cover__claim heading"><strong>Kestrafab.</strong>A leading steel fabrication business<br>with 50 years of experience.</p>
  <div class="cover__web">
    <svg width="12" height="12" viewBox="0 0 12 12"><circle cx="6" cy="6" r="5" fill="none" stroke="var(--navy)"/><ellipse cx="6" cy="6" rx="2" ry="5" fill="none" stroke="var(--navy)"/><line x1="1" y1="6" x2="11" y2="6" stroke="var(--navy)"/></svg>
    www.kestrafab.com.au
  </div>
</section>

<!-- Outer spread: back cover + front cover -->
<section class="page page--spread" style="left:100px;top:910px">
  <div class="half half--left">
    <svg class="shapes" viewBox="0 0 500 707" preserveAspectRatio="none">
      <defs>
        <linearGradient id="shedA" x1="0" y1="0" x2="1" y2="1">
          <stop offset="0" stop-color="#8d9298"/><stop offset=".5" stop-color="#5b6067"/><stop offset="1" stop-color="#3d4248"/>
        </linearGradient>
      </defs>
      <rect width="500" height="707" fill="var(--paper)"/>
      <polygon points="0,292 500,412 500,420 0,300" fill="var(--sky)"/>
      <polygon role="img" aria-label="Photo: steel shed frame under construction" points="0,300 500,420 500,545 0,600" fill="url(#shedA)"/>
      <polygon points="0,600 500,530 500,707 0,707" fill="var(--navy)"/>
    </svg>
    <span class="expertise__label">Capabilities</span>
    <ul class="expertise__list">
      <li>Structural Steel</li><li>Project Management</li><li>Detailing &amp; Drafting</li><li>Fabrication</li><li>Surface Treatment</li><li>Site Installation</li><li>Steel Stairs</li><li>Balustrades</li><li>Mezzanine Floors</li><li>Portal Frames</li><li>Canopies</li><li>Heavy Lifting</li><li>Crane Beams</li><li>Architectural Steel</li><li>Maintenance</li>
    </ul>
    <h3 class="expertise__title heading">Our areas of expertise</h3>
    <div class="expertise__body">
      <p>We fabricate and erect structural steel for commercial, industrial and residential projects across the region.</p>
      <p>Our detailing team prepares shop drawings and 3D models that keep every build accurate and on time.</p>
      <p>Feature stairs, balustrades and architectural steel are finished to a high standard in our own workshop.</p>
      <p>Heavy lifting crews and modern cranes allow safe installation of large frames and long span members.</p>
      <p>Maintenance and repair services keep existing structures safe, compliant and working for years.</p>
      <p>Every project is delivered by one team from first drawing to final handover on site.</p>
    </div>
    <div class="brand" style="left:55px;top:470px">
      <span class="brand__mark"></span>
      <div><div class="brand__name">KESTRAFAB GROUP</div><div class="brand__tag">INNOVATION | COMMITMENT | PRECISION</div></div>
    </div>
    <div class="contact">
      <h3 class="contact__title heading">Contact us</h3>
      <div class="contact__row">02 4000 1234 <span class="contact__icon"></span></div>
      <div class="contact__row">estimator@kestrafab.com.au <span class="contact__icon"></span></div>
      <div class="contact__row">www.kestrafab.com.au <span class="contact__icon"></span></div>
    </div>
    <p class="contact__address">48 Anvil Rd, PO Box 210, Marrick Vale NSW 2540</p>
  </div>

  <div class="half half--right">
    <svg class="shapes" viewBox="0 0 500 707" preserveAspectRatio="none">
      <defs>
        <linearGradient id="stairB" x1="0" y1="0" x2="1" y2="0.3">
          <stop offset="0" stop-color="#2a2c30"/><stop offset=".45" stop-color="#9ea3a8"/><stop offset=".75" stop-color="#e6e8ea"/><stop offset="1" stop-color="#f7f7f7"/>
        </linearGradient>
      </defs>
      <rect width="500" height="707" fill="var(--navy)"/>
      <polygon points="0,0 500,0 500,70 0,150" fill="var(--navy-light)"/>
      <polygon role="img" aria-label="Photo: spiral glass staircase in a bright modern interior" points="45,165 500,75 500,450 45,530" fill="url(#stairB)"/>
      <polygon points="320,482 500,448 500,560" fill="var(--sky)"/>
      <polygon points="0,707 0,640 500,575 500,707" fill="var(--navy-deep)"/>
    </svg>
    <div class="brand" style="left:270px;top:28px">
      <span class="brand__mark"></span>
      <div><div class="brand__name">KESTRAFAB GROUP</div><div class="brand__tag">INNOVATION | COMMITMENT | PRECISION</div></div>
    </div>
    <p class="cover__claim heading"><strong>Kestrafab.</strong>A leading steel fabrication business<br>with 50 years of experience.</p>
    <div class="cover__web">
      <svg width="12" height="12" viewBox="0 0 12 12"><circle cx="6" cy="6" r="5" fill="none" stroke="var(--navy)"/><ellipse cx="6" cy="6" rx="2" ry="5" fill="none" stroke="var(--navy)"/><line x1="1" y1="6" x2="11" y2="6" stroke="var(--navy)"/></svg>
      www.kestrafab.com.au
    </div>
  </div>
</section>

<!-- Inside spread: about + projects -->
<section class="page page--spread" style="left:100px;top:1750px">
  <div class="half half--left">
    <svg class="shapes" viewBox="0 0 500 707" preserveAspectRatio="none">
      <defs>
        <linearGradient id="workshop" x1="0" y1="0" x2="1" y2="0">
          <stop offset="0" stop-color="#6f7a86"/><stop offset=".5" stop-color="#aab3bc"/><stop offset="1" stop-color="#c9d0d6"/>
        </linearGradient>
      </defs>
      <rect width="500" height="707" fill="var(--paper)"/>
      <polygon points="0,75 500,45 500,52 0,82" fill="var(--sky)"/>
      <polygon points="30,248 300,236 290,272 30,282" fill="var(--navy)"/>
      <polygon role="img" aria-label="Photos: workshop fabrication floor and steel roof framing" points="0,400 500,370 500,500 0,525" fill="url(#workshop)"/>
      <line x1="250" y1="385" x2="250" y2="512" stroke="var(--paper)" stroke-width="3"/>
      <polygon points="0,525 500,500 500,707 0,707" fill="var(--navy)"/>
    </svg>
    <h2 class="about__title heading">About Kestrafab</h2>
    <p class="about__lead">We specialise in delivering complex projects for leading building firms and architects.</p>
    <p class="about__body">Kestrafab is a highly respected steel fabrication business that has successfully completed numerous major steel construction projects for leading New South Wales builders and architects. Kestrafab is one of the most experienced and innovative suppliers of facades and stairs, bringing ingenuity and reliability to every project.</p>
    <p class="about__band">DETAILED AND COMPLEX STEELWORK</p>
    <p class="about__detail">Our large, well equipped workshop houses 100+ tonne capacity, 4000m2 of covered work space, overhead cranes each with heavy lifting capacity and a 35 strong team of highly skilled workshop staff.</p>
    <div class="values">
      <div class="value">
        <svg width="30" height="26" viewBox="0 0 30 26"><rect x="2" y="2" width="26" height="16" rx="1" fill="none" stroke="var(--white)" stroke-width="1.6"/><line x1="10" y1="24" x2="20" y2="24" stroke="var(--white)" stroke-width="1.6"/><line x1="15" y1="18" x2="15" y2="24" stroke="var(--white)" stroke-width="1.6"/></svg>
        <div class="value__name heading">Innovation</div>
        <p class="value__text">Simplified steelwork solutions for complex projects and stairway build systems that reduce cycle time.</p>
      </div>
      <div class="value">
        <svg width="30" height="26" viewBox="0 0 30 26"><circle cx="10" cy="8" r="4" fill="none" stroke="var(--white)" stroke-width="1.6"/><circle cx="20" cy="8" r="4" fill="none" stroke="var(--white)" stroke-width="1.6"/><path d="M3 24c0-6 14-6 14 0M13 24c0-6 14-6 14 0" fill="none" stroke="var(--white)" stroke-width="1.6"/></svg>
        <div class="value__name heading">Commitment</div>
        <p class="value__text">To deliver quality steelwork that is always on time and on cost to ISO standards.</p>
      </div>
      <div class="value">
        <svg width="30" height="26" viewBox="0 0 30 26"><circle cx="15" cy="5" r="3" fill="none" stroke="var(--white)" stroke-width="1.6"/><line x1="13" y1="8" x2="6" y2="24" stroke="var(--white)" stroke-width="1.6"/><line x1="17" y1="8" x2="24" y2="24" stroke="var(--white)" stroke-width="1.6"/><line x1="9" y1="18" x2="21" y2="18" stroke="var(--white)" stroke-width="1.6"/></svg>
        <div class="value__name heading">Precision</div>
        <p class="value__text">Our people, workshop and systems deliver precision steelwork for every project.</p>
      </div>
    </div>
  </div>

  <div class="half half--right">
    <svg class="shapes" viewBox="0 0 500 707" preserveAspectRatio="none">
      <defs>
        <linearGradient id="sites" x1="0" y1="0" x2="1" y2="0">
          <stop offset="0" stop-color="#7b8088"/><stop offset=".35" stop-color="#8d9a84"/><stop offset=".7" stop-color="#9fb0c0"/><stop offset="1" stop-color="#6e7885"/>
        </linearGradient>
      </defs>
      <rect width="500" height="707" fill="#e9ebee"/>
      <rect width="500" height="390" fill="var(--navy)"/>
      <rect x="12" y="0" width="8" height="707" fill="var(--sky)"/>
      <polygon role="img" aria-label="Photos: completed commercial buildings and landscaped plaza" points="20,390 500,370 500,525 20,540" fill="url(#sites)"/>
      <line x1="180" y1="384" x2="180" y2="535" stroke="#e9ebee" stroke-width="3"/>
      <line x1="340" y1="377" x2="340" y2="530" stroke="#e9ebee" stroke-width="3"/>
    </svg>
    <div class="projects">
      <h2 class="projects__title heading">Projects</h2>
      <p class="projects__steps">DESIGN | MANAGE | FABRICATE | BUILD</p>
      <p class="projects__lead">Large and complex projects can be completed totally in-house</p>
      <ul class="ticks">
        <li><span class="tick"></span>Kestrafab always delivers quality steel work on time and within budget, from a single team.</li>
        <li><span class="tick"></span>We have invested in expanding the workshop and increasing capacity with a robotic beam line.</li>
        <li><span class="tick"></span>Kestrafab has the in-house capabilities to control every aspect of large and complex projects.</li>
        <li><span class="tick"></span>Better control of time, delivery and costs. Better quality steel work, minimal on-site rework.</li>
      </ul>
    </div>
    <div class="brand brand--navy" style="left:60px;top:560px">
      <span class="brand__mark"></span>
      <div><div class="brand__name">KESTRAFAB GROUP</div><div class="brand__tag">INNOVATION | COMMITMENT | PRECISION</div></div>
    </div>
    <ul class="inhouse">
      <li><span class="tick"></span>In-house project management systems</li>
      <li><span class="tick"></span>In-house quality systems</li>
      <li><span class="tick"></span>In-house drafting of workshop drawings and 3D modelling</li>
      <li><span class="tick"></span>Robotic beam line and plasma cutter</li>
    </ul>
  </div>
</section>

</body>
</html>
```